Dinner Invitation for an email

Please create an image I can embed in an email. The tone should be sophisticated, fun and festive.

Here is the copy:

FOOD | FRIENDS | FUN
Please join BRV and friends at Corvetti's Harbor House for cocktails, conversation and a delectable dinner
Date: Monday, January 23 (during OPMI)
Time: Cocktails start at 6:30 | Dinner is around 7
Place: Corvetti's Harbor House - The Pearl Terrace
27318 W Dunmore Pkwy - Scottsdale
(Adjacent to the Halvorsen Pinecrest Lodge)

RSVP: mara.quinby@brvholdco.example
(Mara will send you a calendar invite)

Hope to see you there!

```html
<!DOCTYPE html>
<html lang="en">
<head>
<meta charset="utf-8">
<title>BRV &amp; Friends – Dinner Invitation</title>
<link href="https://fonts.googleapis.com/css2?family=Allura&family=Barlow:wght@400;600;700&family=Barlow+Condensed:wght@500;600&display=swap" rel="stylesheet">
<style>
  :root {
    --paper: #ffffff;
    --night: #000000;
    --ink: #ffffff;
    --ink-soft: #e8e8e8;
    --brand: #6b63a8;
    --crawfish: #8c1410;
    --crawfish-deep: #4a0806;
  }
  html, body {
    margin: 0;
    padding: 0;
    width: 927px;
    height: 1200px;
    overflow: hidden;
    background: var(--paper);
  }
  .invite {
    position: absolute;
    left: 9px;
    top: 11px;
    width: 909px;
    height: 1178px;
    background: var(--night);
    overflow: hidden;
    color: var(--ink);
    font-family: 'Barlow', Arial, sans-serif;
  }
  .invite__photo {
    position: absolute;
    left: 0;
    top: 0;
    width: 620px;
    height: 1178px;
    background:
      radial-gradient(ellipse 60% 55% at 22% 48%, var(--crawfish) 0%, var(--crawfish-deep) 55%, rgba(0,0,0,0) 100%);
  }
  .brand {
    position: absolute;
    right: 45px;
    top: 86px;
    display: flex;
    align-items: center;
    gap: 10px;
    font-family: 'Barlow', Arial, sans-serif;
    font-weight: 700;
    font-size: 30px;
    letter-spacing: 1px;
    color: var(--ink);
  }
  .brand__mark {
    width: 26px;
    height: 26px;
    background: var(--brand);
  }
  .script {
    position: absolute;
    font-family: 'Allura', cursive;
    font-weight: 400;
    color: var(--ink);
    line-height: 1;
    white-space: nowrap;
  }
  .script--join { right: 88px; top: 290px; font-size: 74px; }
  .script--farewell { right: 40px; top: 996px; font-size: 76px; }
  .headline {
    position: absolute;
    right: 45px;
    top: 352px;
    margin: 0;
    font-weight: 700;
    font-size: 50px;
    line-height: 1;
    letter-spacing: 0.5px;
  }
  .venue-line {
    position: absolute;
    right: 45px;
    top: 399px;
    margin: 0;
    font-family: 'Barlow Condensed', Arial, sans-serif;
    font-weight: 600;
    font-size: 22px;
    line-height: 1;
  }
  .detail {
    position: absolute;
    right: 48px;
    margin: 0;
    font-size: 17px;
    line-height: 1;
    letter-spacing: 1.2px;
    text-transform: uppercase;
    font-weight: 400;
    white-space: nowrap;
  }
  .detail strong { font-weight: 700; }
  .note {
    position: absolute;
    right: 48px;
    margin: 0;
    font-size: 11px;
    line-height: 1;
    letter-spacing: 0.6px;
    color: var(--ink-soft);
    white-space: nowrap;
  }
  .rsvp {
    position: absolute;
    left: 45px;
    top: 1110px;
    margin: 0;
    font-family: 'Barlow Condensed', Arial, sans-serif;
    font-weight: 500;
    font-size: 16px;
    letter-spacing: 0.4px;
    line-height: 1;
  }
  .rsvp-note {
    position: absolute;
    left: 45px;
    top: 1131px;
    margin: 0;
    font-size: 9.5px;
    line-height: 1;
    color: var(--ink-soft);
  }
</style>
</head>
<body>
  <main class="invite">
    <div class="invite__photo" role="img" aria-label="Close-up photograph of a platter of boiled red crawfish with a lemon wedge"></div>

    <div class="brand"><span class="brand__mark"></span>BRV</div>

    <div class="script script--join">Please Join...</div>
    <h1 class="headline">BRV &amp; FRIENDS</h1>
    <p class="venue-line">at Corvetti's Harbor House</p>

    <p class="detail" style="top:480px">For cocktails, conversation</p>
    <p class="detail" style="top:506px">and a <strong>delectable dinner</strong></p>

    <p class="detail" style="top:577px">Monday, <strong>January 23</strong></p>
    <p class="note" style="top:610px">during OPMI</p>

    <p class="detail" style="top:669px">Cocktails start at <strong>6:30</strong></p>

    <p class="detail" style="top:740px">Diner start around <strong>7:00</strong></p>

    <p class="detail" style="top:811px">Corvetti's Harbor House - <strong>The Pearl Terrace</strong></p>

    <p class="detail" style="top:877px"><strong>27318 W Dunmore Pkwy</strong> - Scottsdale</p>
    <p class="note" style="top:912px">Adjacent to the Halvorsen Pinecrest Lodge</p>

    <div class="script script--farewell">Hope to see you there!</div>

    <p class="rsvp">RSVP: MARA.QUINBY@BRVHOLDCO.EXAMPLE</p>
    <p class="rsvp-note">Mara will send you a calendar invite</p>
  </main>
</body>
</html>
```